Online training business needs new website

We need a new wordpress website as a result of a rebranding. The business is a crisis management training company focussed on online training and simulation exercises. We only need a 4 page site - home, about us, contact us and blog. However we must be able to add additional tabs in the header to redirect to our sales and marketing system (Vendolo). As these change from time to time, we must be able to add and delete as required.The site must be editable by us, with a basic understanding of wordpress and no understanding of coding. We don't want to have to employ someone to change text, add posts or add a new workshops etc. The theme chosen must be easy to edit by a beginner.

Target Market(s)

Senior managers food and consumer goods companies

Industry/Entity Type

Consulting

Coding

Coded - Design and coding required

Font styles to use
Sans Serif

Requirements
Must have
• Home page, about us, contact us, blog
• Colour scheme from logo (attached) - maroon, blue and grey
• If you go to the current website "brightfernacademy.com" and click on the "workshops" tab you will see the content I need on the home page for the stormbeacon.com site
Nice to have
• Modern, simple and minimalist design is preferred

```html
<!DOCTYPE html>
<html lang="en">
<head>
<meta charset="utf-8">
<title>Storm Beacon – Blogs</title>
<link href="https://fonts.googleapis.com/css2?family=Roboto:wght@400;500;700&family=Open+Sans:wght@400;600;700&family=Montserrat:wght@500;600&display=swap" rel="stylesheet">
<style>
:root{
  --navy:#0b3566;
  --maroon:#7f0e3f;
  --grey:#5a5a5a;
  --line:#c9c9c9;
  --white:#ffffff;
}
*{margin:0;padding:0;box-sizing:border-box}
html,body{width:1200px;height:3015px;overflow:hidden;background:var(--white)}
body{position:relative;font-family:"Open Sans",Arial,sans-serif;color:var(--grey)}
.abs{position:absolute}

/* header */
.site-header{position:absolute;left:0;top:0;width:1200px;height:112px;background:var(--white);z-index:5}
.brand{position:absolute;left:168px;top:0;width:170px;height:138px;background:var(--white);border-radius:0 0 85px 85px;display:flex;align-items:center;justify-content:center;gap:8px}
.brand-dot{width:18px;height:18px;border-radius:50%;background:var(--maroon)}
.brand-name{font-family:"Roboto",sans-serif;font-weight:700;font-size:22px;color:var(--navy);line-height:1}
.next-workshop{position:absolute;left:630px;top:24px;font-family:"Roboto",sans-serif;font-weight:500;font-size:13px;color:var(--navy);letter-spacing:.2px}
.register-btn{position:absolute;left:932px;top:12px;width:108px;height:38px;border-radius:19px;background:var(--navy);color:var(--white);font-family:"Roboto",sans-serif;font-weight:500;font-size:13px;display:flex;align-items:center;justify-content:center}
.main-nav{position:absolute;left:372px;top:68px;display:flex;gap:22px;font-family:"Roboto",sans-serif;font-size:17px;color:var(--navy)}
.main-nav .current{color:var(--maroon)}

/* hero */
.hero{position:absolute;left:0;top:112px;width:1200px;height:428px;background:linear-gradient(135deg,#2a2b2e 0%,#4a4c50 45%,#2b2d30 100%)}
.hero-title{position:absolute;left:0;top:265px;width:1200px;text-align:center;font-family:"Roboto",sans-serif;font-weight:700;font-size:50px;color:var(--white);z-index:2}
.hero-curve{position:absolute;left:0;top:420px;z-index:2;display:block}

.section-title{position:absolute;left:0;width:1200px;text-align:center;font-family:"Roboto",sans-serif;font-weight:500;font-size:36px;color:var(--maroon);line-height:44px}
.section-title.light{color:var(--white);font-size:31px;font-weight:700}
.section-title.video{font-size:31px;font-weight:700}

/* cards */
.post-card{position:absolute;background:var(--white);border:2px solid var(--line);display:flex;height:244px}
.post-media{height:100%;flex:none}
.post-body{padding:28px 28px 0 30px}
.post-title{font-family:"Montserrat",sans-serif;font-weight:500;font-size:20px;color:var(--navy);margin-bottom:6px}
.post-date{font-family:"Roboto",sans-serif;font-size:13px;color:var(--maroon);margin-bottom:8px}
.post-excerpt{font-size:13px;line-height:23px;color:#444}
.post-more{display:block;margin-top:12px;font-weight:700;font-size:14px;color:var(--maroon)}
.audio .post-body{padding:28px 22px 0 28px}
.audio .post-excerpt{font-size:12.5px;line-height:25px}
.photo-office{background:linear-gradient(120deg,#5c5550,#a09a94 50%,#3e3a38)}
.photo-chart{background:linear-gradient(120deg,#111,#4b4b4b 55%,#1a1a1a)}
.photo-wave{background:radial-gradient(ellipse at 55% 50%,#1e7fe0 0%,#0c2d78 35%,#05092a 75%)}
.photo-laptop{background:linear-gradient(120deg,#6c6c70,#d7d8dc 55%,#9fa3a9)}
.photo-umbrella{background:linear-gradient(180deg,#6d8596,#3a4a57 60%,#1f2a33)}
.play{position:absolute;width:60px;height:60px;border-radius:50%;background:var(--white);display:flex;align-items:center;justify-content:center}

/* footer */
.footer-rule{position:absolute;left:0;top:2866px;width:1200px;height:2px;background:#c6d0dc}
.footer-nav{position:absolute;left:0;top:2901px;width:1200px;display:flex;justify-content:center;gap:22px;font-family:"Roboto",sans-serif;font-size:17px;color:var(--navy)}
.copyright{position:absolute;left:0;top:2940px;width:1200px;text-align:center;font-family:"Roboto",sans-serif;font-size:16px;color:#444}
</style>
</head>
<body>

<header class="site-header">
  <div class="brand"><span class="brand-dot"></span><span class="brand-name">STORM<br>BEACON</span></div>
  <div class="next-workshop">NEXT WORK SHOP -&nbsp; SYDNEY , MELBOURNE</div>
  <div class="register-btn">REGISTER</div>
  <nav class="main-nav">
    <span>ABOUT US</span><span>WORKSHOPS</span><span>ONLINE COURSE</span><span>SIMULATIONS</span><span>CONTACT US</span><span class="current">BLOG</span>
  </nav>
</header>

<section class="hero" role="img" aria-label="Desk with a laptop showing a blog web page"></section>
<h1 class="hero-title">BLOGS</h1>
<svg class="hero-curve" width="1200" height="120" viewBox="0 0 1200 120">
  <path d="M0,116 Q600,20 1200,116 L1200,120 L0,120 Z" fill="#fff"/>
  <path d="M120,96 Q600,48 1080,96" fill="none" stroke="#0b3566" stroke-width="4"/>
  <path d="M80,106 Q600,52 1120,106" fill="none" stroke="#0b3566" stroke-width="1.5"/>
  <circle cx="600" cy="50" r="36" fill="#fff"/>
</svg>

<h2 class="section-title" style="top:550px">RECENT BLOGS</h2>

<article class="post-card" style="left:188px;top:640px;width:806px">
  <div class="post-media photo-office" style="width:402px" role="img" aria-label="Business team discussing documents"></div>
  <div class="post-body">
    <h3 class="post-title">Your Blog Title here</h3>
    <div class="post-date">02 Aug 2017</div>
    <p class="post-excerpt">Aassa libero interdum nec interdum vel blandit sed nulla In ullamcorper est eget tempor cursus neque mi consectetuer mi a ultricies massa est sed nisl Class aptent taciti sociosqu ad litora torquent per conubia</p>
    <span class="post-more">More</span>
  </div>
</article>
<article class="post-card" style="left:188px;top:912px;width:806px">
  <div class="post-media photo-chart" style="width:402px" role="img" aria-label="Businessman drawing a line chart"></div>
  <div class="post-body">
    <h3 class="post-title">Your Blog Title here</h3>
    <div class="post-date">02 Aug 2017</div>
    <p class="post-excerpt">Aassa libero interdum nec interdum vel blandit sed nulla In ullamcorper est eget tempor cursus neque mi consectetuer mi a ultricies massa est sed nisl Class aptent taciti sociosqu ad litora torquent per conubia</p>
    <span class="post-more">More</span>
  </div>
</article>

<svg class="abs" style="left:0;top:1200px" width="1200" height="1000" viewBox="0 0 1200 1000">
  <path d="M0,60 Q650,-30 1200,50 L1200,80 Q600,20 0,120 Z" fill="#7f0e3f"/>
  <path d="M0,120 Q600,20 1200,70 L1200,870 Q700,990 200,920 Q80,900 0,870 Z" fill="#0b3566"/>
  <path d="M200,920 Q700,990 1200,870 L1200,910 Q700,1010 200,920 Z" fill="#7f0e3f"/>
</svg>

<h2 class="section-title light" style="top:1278px">AUDIO BLOGS</h2>

<article class="post-card audio" style="left:220px;top:1344px;width:774px;height:234px;border:none">
  <div class="post-media photo-wave" style="width:384px" role="img" aria-label="Blue sound wave visual"></div>
  <div class="post-body">
    <h3 class="post-title">Audio Blog Title here</h3>
    <p class="post-excerpt">Aassa libero interdum nec interdum vel blandit sed nulla In ullamcorper est eget tempor cursus neque mi consectetuer mi a ultricies massa est sed nisl Class aptent taciti sociosqu ad litora torquent per conubia</p>
    <span class="post-more">More</span>
  </div>
</article>
<article class="post-card audio" style="left:222px;top:1590px;width:774px;height:234px;border:none">
  <div class="post-media photo-wave" style="width:384px" role="img" aria-label="Blue sound wave visual"></div>
  <div class="post-body">
    <h3 class="post-title">Audio Blog Title here</h3>
    <p class="post-excerpt">Aassa libero interdum nec interdum vel blandit sed nulla In ullamcorper est eget tempor cursus neque mi consectetuer mi a ultricies massa est sed nisl Class aptent taciti sociosqu ad litora torquent per conubia</p>
    <span class="post-more">More</span>
  </div>
</article>
<article class="post-card audio" style="left:224px;top:1838px;width:774px;height:234px;border:none">
  <div class="post-media photo-wave" style="width:384px" role="img" aria-label="Blue sound wave visual"></div>
  <div class="post-body">
    <h3 class="post-title">Audio Blog Title here</h3>
    <p class="post-excerpt">Aassa libero interdum nec interdum vel blandit sed nulla In ullamcorper est eget tempor cursus neque mi consectetuer mi a ultricies massa est sed nisl Class aptent taciti sociosqu ad litora torquent per conubia</p>
    <span class="post-more">More</span>
  </div>
</article>

<h2 class="section-title video" style="top:2208px">VIDEO BLOGS</h2>

<article class="post-card" style="left:198px;top:2274px;width:806px">
  <div class="post-media photo-laptop" style="width:402px;position:relative" role="img" aria-label="Stressed worker at a laptop with charts">
    <span class="play" style="left:170px;top:90px"><svg width="22" height="24" viewBox="0 0 22 24"><path d="M3,0 L22,12 L3,24 Z" fill="#111"/></svg></span>
  </div>
  <div class="post-body">
    <h3 class="post-title">Video Blog Title here</h3>
    <p class="post-excerpt">Aassa libero interdum nec interdum vel blandit sed nulla In ullamcorper est eget tempor cursus neque mi consectetuer mi a ultricies massa est sed nisl Class aptent taciti sociosqu ad litora torquent per conubia</p>
    <span class="post-more">More</span>
  </div>
</article>
<article class="post-card" style="left:202px;top:2548px;width:806px">
  <div class="post-media photo-umbrella" style="width:402px;position:relative" role="img" aria-label="Business people with umbrellas in the rain">
    <span class="play" style="left:170px;top:90px"><svg width="22" height="24" viewBox="0 0 22 24"><path d="M3,0 L22,12 L3,24 Z" fill="#111"/></svg></span>
  </div>
  <div class="post-body">
    <h3 class="post-title">Video Blog Title here</h3>
    <p class="post-excerpt">Aassa libero interdum nec interdum vel blandit sed nulla In ullamcorper est eget tempor cursus neque mi consectetuer mi a ultricies massa est sed nisl Class aptent taciti sociosqu ad litora torquent per conubia</p>
    <span class="post-more">More</span>
  </div>
</article>

<footer>
  <div class="footer-rule"></div>
  <nav class="footer-nav">
    <span>ABOUT US</span><span>WORKSHOPS</span><span>ONLINE COURSE</span><span>SIMULATIONS</span><span>CONTACT US</span><span>BLOG</span>
  </nav>
  <p class="copyright">© 2019 Company Name&nbsp; All right reserved</p>
</footer>

</body>
</html>
```